Professional violinist needs business cards

I am trying to attract the following jobs:
-private violin lessons (primarily classical)
-performance gigs (weddings, birthday parties, funerals, etc.)
-collaborations with other artists (studio recordings, performances)

I want to communicate that I have a very high standard of excellence for my work, but I also love people and celebrations.
Values/style words I like are:
love, joy, peace, fun, beauty, authenticity, excellence, warmth, refined/sleek, free spirited. If that's too confusing, just ignore :)

I will attach my favorite business card template that I could find on Canva. The lines are supposed to be like a music staff, which I think is really cool, but I also don't want it to look too busy. I like the simple black and white--I think it looks sharp--but I also am open to other ideas. I also have seen business cards with pictures included that looked great, so I attached an image that could be used as well.

I am also attaching a file that I made of my initials that could be used as a logo, but I'm not sure if it should be included.

Information on the card:
-My name (18 letters total)
-"violinist"
-phone number, email, website

Thank you!

```html
<!DOCTYPE html>
<html lang="en">
<head>
<meta charset="utf-8">
<title>Violinist Business Card – Front and Back</title>
<link href="https://fonts.googleapis.com/css2?family=Archivo+Black&family=Sora:wght@400;600&display=swap" rel="stylesheet">
<style>
  :root {
    --page: #fdfdfd;
    --ink: #0a0a0a;
    --paper: #ffffff;
    --card-border: #e4e4e4;
    --icon-tile: #e6e6e7;
    --divider: #e2e2e2;
    --photo-light: #8a8a8a;
    --photo-dark: #2e2e2e;
    --reverse: #000000;
    --reverse-ink: #ffffff;
  }
  * { margin: 0; padding: 0; box-sizing: border-box; }
  html, body { width: 1200px; height: 1200px; overflow: hidden; }
  body {
    position: relative;
    background: var(--page);
    font-family: "Sora", sans-serif;
    color: var(--ink);
  }
  .side-label {
    position: absolute;
    top: 190px;
    width: 446px;
    text-align: center;
    font-size: 23px;
    font-weight: 400;
    letter-spacing: 0.5px;
  }
  .side-label--front { left: 111px; }
  .side-label--back { left: 667px; }

  .card {
    position: absolute;
    top: 231px;
    width: 446px;
    height: 781px;
    border-radius: 26px;
    overflow: hidden;
  }
  .card--front {
    left: 111px;
    background: var(--paper);
    border: 1.5px solid var(--card-border);
  }
  .card--back {
    left: 667px;
    background: var(--reverse);
    color: var(--reverse-ink);
  }

  .portrait {
    position: absolute;
    left: 0; top: 0;
    width: 100%;
    height: 391px;
    background: radial-gradient(ellipse at 50% 45%, var(--photo-light) 0%, #5a5a5a 45%, var(--photo-dark) 100%);
  }
  .portrait-rule {
    position: absolute;
    left: 86px;
    top: 389px;
    width: 274px;
    height: 5px;
    background: var(--divider);
  }

  .contact-row {
    position: absolute;
    left: 73px;
    display: flex;
    align-items: center;
  }
  .icon-tile {
    width: 43px;
    height: 43px;
    border-radius: 8px;
    background: var(--icon-tile);
    display: flex;
    align-items: center;
    justify-content: center;
    flex-shrink: 0;
  }
  .contact-text {
    margin-left: 30px;
    font-size: 16px;
    line-height: 19px;
  }
  .row-name { top: 447px; }
  .row-phone { top: 516px; }
  .row-email { top: 583px; }
  .row-web { top: 650px; }
  .person-name {
    font-family: "Archivo Black", sans-serif;
    font-size: 21px;
    line-height: 24px;
    letter-spacing: 0.3px;
  }
  .person-role {
    font-size: 17px;
    line-height: 22px;
  }

  .staff-line {
    position: absolute;
    left: 0;
    width: 100%;
    height: 2px;
    background: var(--reverse-ink);
  }
  .emblem {
    position: absolute;
    left: 164px;
    top: 28px;
    width: 125px;
    height: 282px;
    border-radius: 50px 50px 40px 40px;
    background: var(--reverse-ink);
  }

  .services {
    position: absolute;
    top: 345px;
    left: 0;
    width: 100%;
    text-align: center;
    font-size: 16px;
    line-height: 19.5px;
  }
  .services-heading {
    font-size: 19px;
    font-weight: 600;
    letter-spacing: 2px;
    margin-bottom: 18px;
  }
  .service { margin-bottom: 18px; }
  .service-title { font-weight: 600; }
  .service-detail { font-weight: 400; letter-spacing: 0.3px; }

  .back-website {
    position: absolute;
    top: 662px;
    width: 100%;
    text-align: center;
    font-size: 23px;
    letter-spacing: 0.6px;
  }
</style>
</head>
<body>
  <div class="side-label side-label--front">FRONT</div>
  <div class="side-label side-label--back">BACK</div>

  <section class="card card--front">
    <div class="portrait" role="img" aria-label="Black and white portrait of the violinist holding her violin and bow in front of a stone block wall"></div>
    <div class="portrait-rule"></div>

    <div class="contact-row row-name">
      <div class="icon-tile">
        <svg width="22" height="22" viewBox="0 0 24 24" aria-hidden="true"><circle cx="12" cy="7" r="5" fill="#0a0a0a"/><path d="M2 23c0-6 4.5-9 10-9s10 3 10 9z" fill="#0a0a0a"/></svg>
      </div>
      <div class="contact-text">
        <div class="person-name">NAME SURNAME</div>
        <div class="person-role">Violinist</div>
      </div>
    </div>

    <div class="contact-row row-phone">
      <div class="icon-tile">
        <svg width="18" height="28" viewBox="0 0 18 28" aria-hidden="true"><rect x="1" y="1" width="16" height="26" rx="2.5" fill="#0a0a0a"/><rect x="3" y="4.5" width="12" height="17" fill="#e6e6e7"/><circle cx="9" cy="24.2" r="1.4" fill="#e6e6e7"/></svg>
      </div>
      <div class="contact-text">+1 (555) 014 2290<br>+1 (555) 014 2290</div>
    </div>

    <div class="contact-row row-email">
      <div class="icon-tile">
        <svg width="28" height="20" viewBox="0 0 28 20" aria-hidden="true"><rect x="0" y="0" width="28" height="20" rx="2" fill="#0a0a0a"/><path d="M2 3l12 9 12-9" fill="none" stroke="#e6e6e7" stroke-width="2"/></svg>
      </div>
      <div class="contact-text">hello@veranoirstrings.com</div>
    </div>

    <div class="contact-row row-web">
      <div class="icon-tile">
        <svg width="28" height="28" viewBox="0 0 28 28" aria-hidden="true" fill="none" stroke="#0a0a0a" stroke-width="1.6"><circle cx="14" cy="14" r="12.5"/><circle cx="14" cy="14" r="8.5"/><ellipse cx="14" cy="14" rx="3.8" ry="8.5"/><path d="M5.5 14h17M14 5.5v17M7 10h14M7 18h14"/></svg>
      </div>
      <div class="contact-text">www.veranoirstrings.com</div>
    </div>
  </section>

  <section class="card card--back">
    <div class="staff-line" style="top:61px"></div>
    <div class="staff-line" style="top:93px"></div>
    <div class="staff-line" style="top:125px"></div>
    <div class="staff-line" style="top:156px"></div>
    <div class="staff-line" style="top:188px"></div>
    <div class="staff-line" style="top:219px"></div>
    <div class="staff-line" style="top:251px"></div>
    <div class="staff-line" style="top:282px"></div>
    <div class="emblem" role="img" aria-label="White emblem combining a treble clef and a violin silhouette set on the staff lines"></div>

    <div class="services">
      <div class="services-heading">CALL IN FOR:</div>
      <div class="service">
        <div class="service-title">Private Violin Lessons,</div>
        <div class="service-detail">(Primarily Classic)</div>
      </div>
      <div class="service">
        <div class="service-title">Performance Gigs</div>
        <div class="service-detail">(Wedding, Birthday Parties<br>Funerals, Etc.)</div>
      </div>
      <div class="service">
        <div class="service-title">Collaborations With Other Artists</div>
        <div class="service-detail">(Studio Recordings,<br>Performances)</div>
      </div>
    </div>

    <div class="back-website">www.veranoirstrings.com</div>
  </section>
</body>
</html>
```